Updated DJ business Card showing other businesses

DJ Kestro offers professional mobile dj services including DJ. MC. Karaoke.
Silent Disco (will attach logo)
I also offer a 360 Photo Booth.

Contact info:
(555) 314-7720
lenny.corbitt@mailvane.net
Social Media @DJKestroBPZ

```html
<!DOCTYPE html>
<html lang="en">
<head>
<meta charset="utf-8">
<title>DJ Kestro – Business Card</title>
<link rel="stylesheet" href="https://fonts.googleapis.com/css2?family=Montserrat:wght@400;600;800&display=swap">
<style>
  :root {
    --backdrop: #d8d2c9;
    --card-dark: #000000;
    --card-light: #ffffff;
    --accent: #d8204b;
    --ink-light: #ffffff;
    --ink-dark: #0b0b0b;
    --muted: #e6e6e6;
  }
  * { margin: 0; padding: 0; box-sizing: border-box; }
  html, body {
    width: 900px; height: 1200px; overflow: hidden;
    background: var(--backdrop);
    font-family: "Montserrat", sans-serif;
  }
  .canvas { position: relative; width: 900px; height: 1200px; }

  .card {
    position: absolute; left: 80px; width: 742px;
    border-radius: 30px;
    box-shadow: 0 6px 14px rgba(0,0,0,0.35);
  }
  .card--front { top: 130px; height: 445px; background: var(--card-dark); color: var(--ink-light); }
  .card--back { top: 638px; height: 440px; background: var(--card-light); color: var(--ink-dark); }

  .brand-name {
    position: absolute; font-weight: 800; letter-spacing: -1px; line-height: 1; white-space: nowrap;
  }
  .card--front .brand-name { left: 40px; top: 62px; font-size: 66px; color: var(--ink-light); }
  .card--back .brand-name {
    left: 0; right: 0; top: 78px; text-align: center; font-size: 98px; color: var(--ink-dark);
  }

  .role { position: absolute; left: 40px; top: 266px; }
  .role__title { font-size: 24px; font-weight: 600; color: var(--accent); line-height: 1.1; }
  .role__subtitle { font-size: 16px; font-weight: 400; color: var(--ink-light); margin-top: 4px; }

  .divider {
    position: absolute; left: 38px; top: 329px; width: 652px; height: 2px; background: var(--accent);
  }

  .contact { position: absolute; left: 40px; top: 340px; list-style: none; }
  .contact__item {
    display: flex; align-items: center; gap: 9px;
    font-size: 16px; line-height: 22.5px; color: var(--muted);
  }
  .contact__icon { width: 13px; height: 13px; flex: none; fill: var(--accent); }
  .contact__dot { width: 14px; height: 14px; border-radius: 50%; background: var(--accent); flex: none; }

  .sub-brand {
    position: absolute; left: 0; right: 0; top: 232px;
    display: flex; justify-content: center; align-items: center; gap: 18px;
  }
  .sub-brand__circle {
    width: 90px; height: 90px; border-radius: 50%; border: 4px solid var(--ink-dark);
  }
  .sub-brand__name {
    font-size: 58px; font-weight: 800; color: var(--ink-dark); letter-spacing: -1px; line-height: 1;
  }
</style>
</head>
<body>
<main class="canvas">
  <section class="card card--front">
    <div class="brand-name">DJ Kestro</div>

    <div class="role">
      <div class="role__title">MC. Karaoke</div>
      <div class="role__subtitle">Artist</div>
    </div>

    <div class="divider"></div>

    <ul class="contact">
      <li class="contact__item">
        <svg class="contact__icon" viewBox="0 0 16 16" aria-hidden="true">
          <path d="M1 5c0-2 3-3.5 7-3.5S15 3 15 5v1.5h-3.5V5h-7v1.5H1z"/>
          <path d="M3 8h10l1.5 6h-13z"/>
        </svg>
        <span>(555) 314-7720</span>
      </li>
      <li class="contact__item">
        <svg class="contact__icon" viewBox="0 0 16 16" aria-hidden="true">
          <path d="M1 3h14v1.5L8 9 1 4.5z"/>
          <path d="M1 6.3 8 10.8l7-4.5V13H1z"/>
        </svg>
        <span>lenny.corbitt@mailvane.net</span>
      </li>
      <li class="contact__item">
        <span class="contact__dot" aria-hidden="true"></span>
        <span>@DJKestroBPZ</span>
      </li>
    </ul>
  </section>

  <section class="card card--back">
    <div class="brand-name">DJ Kestro</div>
    <div class="sub-brand">
      <span class="sub-brand__circle" aria-hidden="true"></span>
      <span class="sub-brand__name">Silent Disco</span>
    </div>
  </section>
</main>
</body>
</html>
```